Vorlen - Customer Experience Software Company Web Design

*****UPDATE*****
We've been getting a lot of corporate designs through. Unfortunately this is not what we are looking for. We would like our brand to be more approachable and for the look and feel to to be a bit more fun.
Also the best designs we have received so far have followed the "less is more" approach. Im hoping any news designs will take these aspects into account.
*****************

Background:

Vorlen is a Customer Experience Technology company. We equip business and technology teams with the frameworks, tools and services to help them create compelling experiences for their customers.

Our flagship product - Vorlen CX is an open-source customer experience application framework – it enables organisation to build highly differentiated business applications to deliver compelling experiences to your customers.

Vorlen CX is designed for innovators who understand that unlocking opportunity in today’s competitive marketplace is driven by delivering a better customer experience.

Task:

We are looking for a web design (we need PSD, no HTML/CSS) for our company site through which to launch our customer experience framework product. The site will be also used as a support site, so the functional aspect of the site is as important as the visual impact for sales.

In order to help us conceptualise ideas and content we have drafted a temporary website using a standard wordpress theme (please see details below). Now we have a general idea of our requirements we like we would like to take it to the next level and get some designs with that professional edge.

Our target market are Enterprise organisations - that is senior members of the business & technology teams (Business General Managers, CTO’s, CIO’s, and Senior Architects and Senior Developers). We want something clean & fresh which is DIFFERENT from the typical corporate technology websites out there. We would like to be seen as more approachable than most large technology companies.

Words we would like to use to describe the finished design:
• Clean (we’re thinking white background with one or two key colours)
• Fresh
• Light
• Modern
• Less is more
• Web 2.0
• Fun but professional (aimed at Enterprise/Large organisations)
• Bold, clear call to action – e.g. Live Demo & Download
• Readable (but Sans Serif)

As we’re a Customer Experience company, the usability of the site is critical. The site must be functional, intuitive & easy to navigate. We want to keep the number of user clicks to the bare minimum possible.

Other aspects, which we would like to incorporate into the site
• Home Page banner slider
• Client logon
• Newsletter sign up
• Social media links – plain square, plain square (for starters)
• Rich footer links

Some websites we like
• http://brightpanelworks.example - clean, light, modern & intuitive
• http://www.tamsoledrik.example - bold, clear messaging
• http://www.opengridhub.example/markup/emblem - punchy, colourful
• http://postwren.example/ - modern, clear messaging, colourful, rich footer area

Target Market(s)

Enterprise organisations - that is senior members of the business & technology teams (Business General Managers, CTO’s, CIO’s, Senior Devs)

Industry/Entity Type

Business

Requirements
Must have
• - Design Specs: Accepted file formats: During the design phase adobe PSD or JPEG are OK (if you need to upload files), but for the handover we'll need PSD only with all the original layers.
- The width needs to be a size that will work with every size computer screen
- Need to use cross-platform compatible font
- The graphic elements used for the design must be copyright free

Current test site
- URL http://vorlen.example/wp-admin
- username: artmarket
- password: artmarket

IMPORTANT NOTE REGARDING OUR CURRENT TEST SITE:

This is a very basic version of a site to help us generate requirements. This design is only a starting point/input and is not locked in stone i.e. we do not simply want this site simply tweaked around the edges.

We are looking for you to use all of your graphic design skills and experience to create a truly awesome site design!

```html
<!DOCTYPE html>
<html lang="en">
<head>
<meta charset="utf-8">
<title>Vorlen – The Customer Experience Framework</title>
<link href="https://fonts.googleapis.com/css2?family=Open+Sans:wght@400;600&family=Oswald:wght@400;500&display=swap" rel="stylesheet">
<style>
:root{
  --red:#a3121a;
  --red-dark:#7d0a10;
  --text:#333;
  --muted:#7a7a7a;
  --band:#ebebeb;
  --footer:#232323;
  --footer-text:#e6e6e6;
  --footer-muted:#8a8a8a;
  --topbar:#5b5b5b;
}
*{box-sizing:border-box;margin:0;padding:0}
html,body{width:1072px;height:1200px;overflow:hidden;background:#fff}
body{position:relative;font-family:"Open Sans",Arial,sans-serif;color:var(--text)}
a{color:inherit;text-decoration:none}
.topbar{position:absolute;left:0;top:0;width:1072px;height:7px;background:var(--topbar)}

.brand{position:absolute;left:107px;top:28px;display:flex;align-items:center;gap:6px}
.brand-name{font-family:"Open Sans",sans-serif;font-size:38px;font-weight:400;color:var(--red);line-height:1;letter-spacing:-1px}
.brand-mark{width:26px;height:26px;background:#9cbf2b;margin-top:4px}
.brand-tag{position:absolute;left:107px;top:72px;font-size:9.5px;color:#555}

.nav{position:absolute;top:41px;left:528px;display:flex;list-style:none}
.nav li{font-size:12.5px;color:#666;height:21px;line-height:21px}
.nav .home{width:72px;text-align:center;background:#ececec;border:1px solid #d6d6d6;border-radius:4px;color:#444}
.nav .products{margin-left:43px}
.nav .support{margin-left:48px}
.nav .blog{margin-left:53px}
.nav .about{margin-left:40px}

.hero-copy{position:absolute;left:109px;top:134px;width:310px;font-size:14.5px;line-height:26.8px;color:#333}
.btn-download{position:absolute;left:107px;top:289px;width:259px;height:59px;background:linear-gradient(#c4252b,#951015);border:1px solid var(--red-dark);border-radius:3px;display:flex;align-items:center;justify-content:center;font-family:"Oswald",sans-serif;font-size:34px;font-weight:500;color:#f1f1f1;letter-spacing:.5px}
.demo-line{position:absolute;left:107px;top:355px;width:259px;text-align:center;font-size:20px;color:#444}
.demo-line a{color:var(--red)}
.hero-screen{position:absolute;left:432px;top:103px;width:518px;height:334px;background:#1a1a1a;border-radius:14px 14px 0 0;padding:16px 16px 0}
.hero-screen .shot{width:100%;height:100%;background:linear-gradient(#dfe7f3 0,#f4f6f9 18%,#fff 100%)}

.services{position:absolute;left:0;top:437px;width:1072px;height:220px;background:var(--band)}
.service{position:absolute;top:14px;font-size:10.7px;line-height:17.9px;color:var(--muted)}
.service h2{font-size:14px;font-weight:400;color:#333;margin-bottom:7px;letter-spacing:.1px}
.service .art{float:left;width:72px;height:56px;margin:0 10px 4px 0;border-radius:3px}
.s1{left:106px;width:260px}
.s1 .art{background:linear-gradient(135deg,#3a79c9,#9cc3ec)}
.s2{left:409px;width:260px}
.s2 .art{width:56px;background:linear-gradient(135deg,#c8ccd2,#7d8794)}
.s3{left:711px;width:250px}
.s3 .art{width:66px;background:linear-gradient(135deg,#c79a5c,#58a860)}

.section-title{position:absolute;left:106px;top:680px;font-size:14px;font-weight:400;color:#333}
.copy{position:absolute;font-size:10.4px;line-height:16.1px;color:var(--muted)}
.copy p{margin-bottom:16px}
.copy h3{font-size:10px;font-weight:400;color:#d11919;margin:22px 0 13px}
.col-left{left:108px;top:709px;width:405px}
.col-right{left:546px;top:686px;width:405px}
.col-right h3:first-child{margin-top:0}
.btn-more{display:inline-block;margin-top:8px;width:81px;height:22px;line-height:22px;text-align:center;background:linear-gradient(#c4252b,#951015);border-radius:3px;font-family:"Oswald",sans-serif;font-size:12.5px;color:#fff}

.footer{position:absolute;left:0;top:993px;width:1072px;height:207px;background:var(--footer)}
.fcol{position:absolute;top:32px;font-size:9.8px;color:var(--footer-text)}
.fcol h4{font-size:10.5px;font-weight:400;color:#bdbdbd;letter-spacing:.3px;margin-bottom:7px}
.fcol ul{list-style:none}
.fcol li{line-height:16.1px}
.f1{left:106px}.f2{left:315px}.f3{left:507px}.f4{left:725px;width:240px}
.email{width:239px;height:26px;background:#fff;border-radius:3px;font-size:9px;color:#333;padding-left:7px;line-height:26px}
.sub-row{display:flex;align-items:center;margin-top:10px}
.btn-sub{width:79px;height:20px;line-height:20px;text-align:center;background:linear-gradient(#c4252b,#951015);border-radius:3px;font-family:"Oswald",sans-serif;font-size:12.5px;color:#fff}
.follow{font-size:8.5px;color:#aaa;margin:0 4px 0 6px}
.social{width:21px;height:21px;border-radius:3px;margin-left:7px}
.social.a{background:#3b5a9a}.social.b{background:#2fa6d9}.social.c{background:#c5221f}.social.d{background:#1a6fab}
.rule{position:absolute;left:106px;top:1150px;width:858px;height:1px;background:#444}
.copyright{position:absolute;left:107px;top:1161px;font-size:9.5px;color:var(--footer-muted)}
.copyright strong{color:#ddd;font-weight:400}
.legal{position:absolute;right:108px;top:1161px;font-size:9.5px;color:#ddd}
.legal span{color:#777;margin:0 7px}
</style>
</head>
<body>
<div class="topbar"></div>

<header>
  <div class="brand"><span class="brand-name">VORLEN</span><span class="brand-mark"></span></div>
  <div class="brand-tag">The Customer Experience Framework</div>
  <ul class="nav">
    <li class="home">Home</li>
    <li class="products">Products</li>
    <li class="support">Support</li>
    <li class="blog">Blog</li>
    <li class="about">About</li>
  </ul>
</header>

<section class="hero">
  <p class="hero-copy">Vorlen CX is a customer experience application framework – it enables you to build highly differentiated business applications to deliver compelling experiences to your customers.</p>
  <a class="btn-download" href="#">DOWNLOAD</a>
  <p class="demo-line">or try our <a href="#">live demo</a></p>
  <div class="hero-screen"><div class="shot" role="img" aria-label="Screenshot of the Vorlen CX application showing a dashboard with line and area charts"></div></div>
</section>

<section class="services">
  <div class="service s1">
    <h2>APPLICATION ARCHITECTURE SERVICES</h2>
    <div class="art" role="img" aria-label="Illustration of a blueprint map with a compass"></div>
    When building a new application its important to start on the right track. Our expert team can provide trusted technical advice that enables you to optimize for performance, scalability, maintainability, and excellent user experience.
  </div>
  <div class="service s2">
    <h2>UI DESIGN AND DEVELOPMENT</h2>
    <div class="art" role="img" aria-label="Illustration of drafting tools"></div>
    Our designers and developers can help you take your mobile or web app user interface ideas from concept to reality. Whether it’s a brand new application, or a rebuild of a legacy system, we’re ready to give you the look, feel, and functionality that your users and customers need.
  </div>
  <div class="service s3">
    <h2>DEVELOPMENT TEAM MENTORING</h2>
    <div class="art" role="img" aria-label="Illustration of a green chalkboard"></div>
    Our team can work directly with your team on your development project. Best-practice development, performance tuning, code reviews, and pair programming are just some of the ways we can assist on an on-site or off-site basis to make sure your project stays on track. Your team learns valuable on-the-job skills, and your customers get the awesome experience they deserve.
  </div>
</section>

<h2 class="section-title">CREATE COMPELLING EXPERIENCES FOR YOUR CUSTOMERS</h2>
<div class="copy col-left">
  <p>Vorlen is a customer experience application framework – it enables you to build highly differentiated business applications to deliver compelling experiences to your customers.</p>
  <p>Vorlen is designed for innovators who understand that unlocking opportunity in today’s competitive marketplace is driven by delivering a better customer experience.</p>
  <h3>CREATE COMPELLING EXPERIENCES FOR YOUR CUSTOMERS</h3>
  <p>Turn the experience you deliver to your customers into competitive advantage. Vorlen’s customer experience framework is the flexible and practical way for enterprise organisations to create and manage compelling experiences. It gives you full control over how you wish to interact with your customers, and allows you to tailor experiences that grow your brand.</p>
</div>
<div class="copy col-right">
  <h3>TRUE DIFFERENTIATION</h3>
  <p>There is no one-size-fits-all application, because every business is unique! We believe in technology as a business differentiator, and flexible, cutting edge technology the key to success. If you’re serious about differentiation, and want to create powerful experiences to connect with your customers in exciting new ways, we can help create experiences that your competitors can’t match.</p>
  <h3>ENTERPRISE CX</h3>
  <p>Turn the experience you deliver to your customers into competitive advantage. Vorlen’s customer experience framework is the flexible and practical way for enterprise organisations to create and manage compelling experiences. It gives you full control over how you wish to interact with your customers, and allows you to tailor experiences that grow your brand.</p>
  <a class="btn-more" href="#">READ MORE</a>
</div>

<footer class="footer-wrap">
  <div class="footer"></div>
  <div class="fcol f1" style="top:1025px"><h4>VORLEN FRAMEWORK</h4><ul><li>Home</li><li>Products</li><li>Support</li><li>Blog</li><li>About</li></ul></div>
  <div class="fcol f2" style="top:1025px"><h4>GETTING STARTED</h4><ul><li>Demo</li><li>Documentation</li><li>Download</li></ul></div>
  <div class="fcol f3" style="top:1025px"><h4>SUPPORT</h4><ul><li>Contact Us</li><li>Vorlen Services</li><li>Vorlen Support</li></ul></div>
  <div class="fcol f4" style="top:1025px">
    <h4>SUBSCRIBE TO OUR NEWSLETTER</h4>
    <div class="email">EMAIL ADDRESS</div>
    <div class="sub-row">
      <span class="btn-sub">SUBSCRIBE</span><span class="follow">FOLLOW US</span>
      <span class="social a" aria-label="Social network link"></span>
      <span class="social b" aria-label="Social network link"></span>
      <span class="social c" aria-label="Video channel link"></span>
      <span class="social d" aria-label="Professional network link"></span>
    </div>
  </div>
  <div class="rule"></div>
  <p class="copyright">Copyright © 2011 <strong>Vorlen</strong> - Customer Experience Software Company . All Rights Reserved.</p>
  <p class="legal">Terms of Use<span>|</span>Privacy Policy<span>|</span>Copyright Policy</p>
</footer>
</body>
</html>
```